Short term Rentals Marketing agency needs Web design.

We Need a web design for our new company based in Calgary, AB. We are a International Luxury home sharing company (short term rental properties, Villas, Boutique Hotels, Bed & Breakfast, Realtors, Mortgage Brokers). We would like to see designs that look simple, modern and professional. Colors would be bold (red, black, white). The final design should communicate something welcoming, symbolize innovation, and growth. Our goal is to form partnerships with Real Estate, Property Management, Short term Rental Clients to make their lives easier and increase revenue. Vlto Harbor Co. offers a flexible and secure way to market our clients properties while maintaining client satisfaction and amazing customer service. We like how https://brinkleafpromo.ca/ is interactive (when you scroll down, text gets larger). Other similar websites for Short Term Rentals is https://www.quillnestgroup.com/, https://dwelvaroo.com/, https://www.kipmarsh.com/, https://www.tarnpenny.com/about-us/, https://vantrelstays.com. We have attached our Logo.

Target Market(s)

short term rental properties, Villas, Boutique Hotels, Bed & Breakfast, Realtors, Mortgage Brokers, property owners

Industry/Entity Type

Real Estate

Coding

Coded - Design and coding required

Number of Pages Required

5+ page

Font styles to use
Sans Serif

Requirements
Must have
• Home Page, About Us page, How it works, Services, Contact us.

We like how https://brinkleafpromo.ca/ is interactive (when you scroll down, text gets larger).

We have attached our Webcopy. We would like Call to Action Buttons where they're located in the copy and page.

Must have our Logo Colors.

Other similar websites for Short Term Rentals is https://www.quillnestgroup.com/, https://dwelvaroo.com/, https://www.kipmarsh.com/, https://www.tarnpenny.com/about-us/, https://vantrelstays.com.
Nice to have
• Catchy, Interactive Home page.

Should not have
• Should not be too cluttered

```html
<!DOCTYPE html>
<html lang="en">
<head>
<meta charset="utf-8">
<title>Vlto Harbor Co. — Short Term Rental Marketing</title>
<link href="https://fonts.googleapis.com/css2?family=Lato:wght@400;700&family=Playfair+Display:wght@500;600&display=swap" rel="stylesheet">
<style>
:root{
  --red:#e21d2b;
  --ink:#1d1d1f;
  --text:#3a3a3c;
  --muted:#6b6b70;
  --line:#8a8a8f;
  --soft:#f8f9fb;
  --white:#ffffff;
  --sky1:#dfe9f3;
  --sky2:#b9cde0;
}
*{box-sizing:border-box;margin:0;padding:0}
html,body{width:1200px;height:4116px;overflow:hidden;background:var(--white)}
body{position:relative;font-family:"Lato",sans-serif;color:var(--text);font-size:16px}
.abs{position:absolute}
.serif{font-family:"Playfair Display",serif;color:var(--ink);font-weight:600;letter-spacing:.3px}
.band{position:absolute;left:0;width:1200px}
.soft{background:var(--soft)}
.photo{position:absolute}

/* header */
.brand{left:56px;top:22px;display:flex;align-items:center;gap:8px;font-size:20px;font-weight:700;color:var(--ink)}
.brand-mark{width:20px;height:20px;border:3px solid var(--red)}
.nav{top:36px;font-size:15px;color:var(--text)}
.btn-outline{border:1.5px solid var(--line);color:var(--text);font-size:15px;display:flex;align-items:center;justify-content:center;background:transparent}
.btn-red{background:var(--red);color:var(--white);font-size:15px;display:flex;align-items:center;justify-content:center}

.hero-photo{left:0;top:0;width:543px;height:572px;background:linear-gradient(180deg,#b8c7d6 0%,#d9e1e9 45%,#eef1f4 75%,#e6eaee 100%)}
.hero-title{left:626px;top:178px;font-size:38px;line-height:44px}
.hero-lead{left:626px;top:280px;width:420px;font-size:17px;line-height:24px}

.section-title{font-size:36px;line-height:44px;text-align:center;width:1200px;left:0}
.intro{left:90px;width:1020px;top:714px;text-align:center;font-size:17px;line-height:24px}

.feature{top:848px;width:197px;height:82px;border:1.5px solid var(--line);display:flex;align-items:center;gap:12px;padding:0 12px 0 14px;font-size:13.5px;line-height:19px;color:var(--text);background:var(--white)}
.feature svg{flex:none}

.text-link{color:var(--red);font-size:17px;display:flex;align-items:center;gap:10px;border-bottom:1.5px solid var(--red);padding-bottom:3px}
.text-link span.ring{width:12px;height:12px;border:1.5px solid var(--red);border-radius:50%;position:relative}
.text-link span.ring:after{content:"";position:absolute;left:3px;top:3px;width:3px;height:3px;background:var(--red);border-radius:50%}

.h2{font-size:38px;line-height:46px}
.body{font-size:17px;line-height:24px}

.rates-bg{top:1667px;height:369px;background:linear-gradient(100deg,#e9eff6 0%,#e4ecf4 40%,#c9dbea 55%,#e6edf4 75%,#eef2f7 100%)}
.contact-bg{top:3214px;height:508px;background:linear-gradient(100deg,#e6eef6 0%,#dbe6f1 55%,#a9c3dc 75%,#6f97bd 100%)}

.field{border:1.5px solid var(--line);background:transparent;font-size:15px;color:var(--text);padding:10px 14px;line-height:18px}

.foot-h{top:3813px;font-size:22px;font-family:"Playfair Display",serif;color:var(--ink);font-weight:500}
.foot-l{font-size:16px;color:var(--text)}
.social{top:3869px;width:24px;height:24px;border-radius:50%;background:var(--ink)}
.social.red{background:var(--red)}
.rule{left:0;top:4017px;width:1200px;height:1px;background:#c9c9cd}
.fine{top:4050px;font-size:16px;color:var(--muted)}
</style>
</head>
<body>

<!-- Header & hero -->
<div class="hero-photo photo" role="img" aria-label="City skyscrapers rising above a sea of clouds"></div>
<div class="abs brand"><span class="brand-mark"></span>Vlto Harbor Co.</div>
<nav>
  <a class="abs nav" style="left:625px">About us</a>
  <a class="abs nav" style="left:732px">Our Services</a>
  <a class="abs nav" style="left:863px">How it works</a>
  <a class="abs btn-outline" style="left:999px;top:27px;width:149px;height:37px">Contact Us</a>
</nav>
<h1 class="abs serif hero-title">Partner with Us and Let’s<br>Start Growing Together!</h1>
<p class="abs hero-lead">Make your lives easier and increase revenues for your Short term Rental properties.</p>
<a class="abs btn-red" style="left:626px;top:353px;width:170px;height:35px">Work with us</a>
<a class="abs btn-outline" style="left:813px;top:353px;width:170px;height:35px">Learn more</a>

<!-- Marketing intro -->
<section class="band soft" style="top:572px;height:507px"></section>
<h2 class="abs serif section-title" style="top:646px">We Market Your Short Term Properties</h2>
<p class="abs intro">We are here to manage and market your short-term rental properties. Enjoy peace of mind in knowing your short-term rental properties, vacation homes, villas,hotels, and B&amp;Bs are safe, secure, and profitable - no matter&nbsp; where you are in the world. We will help you market, manage, and capitalize on everything, from your newest bookings to house cleaning and upkeep. Let us help you increase your rental revenue&nbsp; by doing the following.</p>

<div class="abs feature" style="left:177px">
  <svg width="36" height="34" viewBox="0 0 36 34" fill="none" stroke="#1d1d1f" stroke-width="1.4"><path d="M6 16 18 5l12 11"/><path d="M9 14v16h18V14"/><path d="M14 23l8-8" stroke="#e21d2b"/><circle cx="15" cy="17" r="1.6" stroke="#e21d2b"/><circle cx="21" cy="22" r="1.6" stroke="#e21d2b"/></svg>
  <span>Increasing your occupancy</span>
</div>
<div class="abs feature" style="left:393px">
  <svg width="36" height="30" viewBox="0 0 36 30" fill="none" stroke="#1d1d1f" stroke-width="1.4"><rect x="5" y="4" width="26" height="17"/><path d="M2 25h32"/><path d="M11 13l4 4 9-8" stroke="#e21d2b"/></svg>
  <span>Streamlining your bookings</span>
</div>
<div class="abs feature" style="left:610px">
  <svg width="36" height="34" viewBox="0 0 36 34" fill="none" stroke="#1d1d1f" stroke-width="1.4"><path d="M18 4v28"/><rect x="5" y="8" width="26" height="12"/><path d="M10 16l3-4 3 4" stroke="#e21d2b"/><path d="M20 12h7M20 16h7" stroke="#e21d2b"/></svg>
  <span>Getting amazing exposure</span>
</div>
<div class="abs feature" style="left:826px">
  <svg width="36" height="34" viewBox="0 0 36 34" fill="none" stroke="#1d1d1f" stroke-width="1.4"><path d="M5 15 18 4l13 11v15H5z"/><path d="M18 26s-7-4-7-9a3.5 3.5 0 0 1 7-1 3.5 3.5 0 0 1 7 1c0 5-7 9-7 9z" stroke="#e21d2b"/></svg>
  <span>Property incredible year-round.</span>
</div>
<a class="abs text-link" style="left:551px;top:978px">About us <span class="ring"></span></a>

<!-- Revenue -->
<div class="photo" style="left:83px;top:1154px;width:432px;height:438px;background:linear-gradient(160deg,#c9d6e2 0%,#aab8c6 40%,#4c5560 75%,#6f6a63 100%)" role="img" aria-label="Two businessmen in suits reviewing a chart in a bright office lounge"></div>
<h2 class="abs serif h2" style="left:601px;top:1214px">Increase Your Revenue<br>(without the hassle)</h2>
<p class="abs body" style="left:601px;top:1332px;width:500px">Having Vlto Harbor Co . manage and market your rental property lets you benefit fromincreased revenues without having to put in the hours of work yourself. Vlto Harbor Co. willmanage your property listings, advertise your listings, optimize your rental pricing, increase your occupancy, and help you offer the very best customer experience.</p>
<a class="abs text-link" style="left:602px;top:1492px">Learn more <span class="ring"></span></a>

<!-- Rates -->
<div class="band rates-bg" role="img" aria-label="Glass tower façade against a pale sky"></div>
<svg class="abs" style="left:557px;top:1754px" width="46" height="40" viewBox="0 0 46 40" fill="none" stroke="#1d1d1f" stroke-width="1.6"><path d="M4 38h38"/><rect x="15" y="8" width="16" height="30"/><path d="M19 4h8v4"/><rect x="6" y="18" width="9" height="20"/><rect x="31" y="18" width="9" height="20"/><path d="M19 14v20M23 14v20M27 14v20"/></svg>
<h2 class="abs serif section-title" style="top:1808px">We have Competitive Rates</h2>
<p class="abs body" style="left:120px;width:960px;top:1874px;text-align:center">We won’t charge you a fixed monthly retainer! Instead, we work on a commission-based system to give you a great hands-off opportunity. We charge 30% of the gross revenue your unit brings in permonth. For example, if we’ve made $1,000,000 in a month on your property, you’ll take home$700,000 and we’ll only take $300,000!</p>

<!-- Support -->
<h2 class="abs serif h2" style="left:110px;top:2194px">Receive Constant Support</h2>
<p class="abs body" style="left:110px;top:2263px;width:400px">Our dedicated team is there to take care of your property so that you don’t have to. Our affordable and professional services include being there to support your guests, constant technical communication, and on-site operations management.</p>
<a class="abs text-link" style="left:110px;top:2431px;gap:22px">Learn more <span class="ring"></span></a>
<div class="photo" style="left:633px;top:2111px;width:431px;height:439px;background:linear-gradient(150deg,#e4e3e1 0%,#cfcdca 45%,#7d7a76 75%,#ecebe8 100%)" role="img" aria-label="Businessman shaking hands with a client across a desk with laptops and coffee cups"></div>

<!-- Risks -->
<section class="band soft" style="top:2626px;height:588px"></section>
<div class="photo" style="left:104px;top:2701px;width:431px;height:438px;background:linear-gradient(170deg,#4a78b8 0%,#6e96cc 45%,#c9d3de 70%,#2f4d78 100%)" role="img" aria-label="Modern apartment tower with stacked white balconies against a blue sky"></div>
<h2 class="abs serif h2" style="left:626px;top:2766px">Manage Your Risks<br>and Insurance</h2>
<p class="abs body" style="left:626px;top:2886px;width:400px">Vlto Harbor Co. will help you protect your property income by giving you the security and insurance you need when it comes to pricing and managing your security deposits. Please note that terms and conditions apply.</p>
<a class="abs text-link" style="left:634px;top:3029px">Work with us <span class="ring"></span></a>

<!-- Contact -->
<div class="band contact-bg" role="img" aria-label="Blue glass skyscraper rising into a pale sky"></div>
<h2 class="abs serif h2" style="left:56px;top:3285px">Contact Us Today</h2>
<div class="abs field" style="left:56px;top:3357px;width:248px;height:39px">Name</div>
<div class="abs field" style="left:329px;top:3357px;width:248px;height:39px">Email</div>
<div class="abs field" style="left:56px;top:3413px;width:521px;height:39px">Phone Number</div>
<div class="abs field" style="left:56px;top:3466px;width:521px;height:128px">Message</div>
<p class="abs" style="left:56px;top:3621px;font-size:13px;color:var(--text)">By Sending I agree to terms and conditions</p>
<a class="abs btn-red" style="left:407px;top:3611px;width:170px;height:37px">Send</a>

<!-- Footer -->
<footer>
  <h3 class="abs foot-h" style="left:56px">Company</h3>
  <a class="abs foot-l" style="left:57px;top:3868px">About Us</a>
  <a class="abs foot-l" style="left:57px;top:3900px">Services</a>
  <a class="abs foot-l" style="left:57px;top:3933px">How it works</a>
  <a class="abs foot-l" style="left:57px;top:3965px">Contact</a>

  <h3 class="abs foot-h" style="left:332px">Inspiration</h3>
  <a class="abs foot-l" style="left:332px;top:3868px">Blog</a>
  <a class="abs foot-l" style="left:332px;top:3900px">Gallary</a>
  <a class="abs foot-l" style="left:332px;top:3933px">Testimonials</a>

  <h3 class="abs foot-h" style="left:614px">Help</h3>
  <a class="abs foot-l" style="left:614px;top:3868px">FAQS</a>
  <a class="abs foot-l" style="left:614px;top:3900px">Customers support</a>

  <h3 class="abs foot-h" style="left:858px">Social media</h3>
  <span class="abs social red" style="left:859px" aria-label="Social profile"></span>
  <span class="abs social" style="left:904px" aria-label="Social profile"></span>
  <span class="abs social" style="left:949px" aria-label="Social profile"></span>

  <div class="abs rule"></div>
  <a class="abs fine" style="left:56px">Privacy Policy</a>
  <a class="abs fine" style="left:181px">Customer Agreement</a>
  <p class="abs fine" style="right:52px">© 2020 All Rights Reserved</p>
</footer>

</body>
</html>
```